Vodka Passionfruit - Design Tavrin Distillery's Canned Beverage

We need help designing the graphic for a canned beverage.

We are a Distillery called Tavrin Distillery based in Bunbury, Western Australia.

"Tavrin" is the latin word for Copper and we use really unique copper pot stills in producing our products. The copper is a common theme throughout our branding so we'd love the primary colour of the can to be copper.

The beverage is a passionfruit vodka using real fruit and no artifical flavours along with our premium triple distilled Vodka. We need it to be noticeable from behind a bar what the flavour is so we'd like some passionfruit's or a passionfruit bursting on the front of the can.

We did a few concepts on ChatGPT and rather liked the one that is attached however as always it looks very grainy and generic.

The can is a 375ml Can that wraps around so a large front panel and smaller back panel would look great. On the front we need our Logo "Tavrin Distillery" (attached) - the words "Vodka Passionfruit" - "375mls" & "4%ABV"

On the back panel we are needing a simple blurb that says "Crafted with Tavrin Distillery's premium Vodka and real passionfruit from Kemberlo Fields, this refreshing blend contains no artificial flavours - just pure, vibrant passionfruit and exceptional craft spirit in every sip."

We need a barcode (attached)
Pregnancy Warning (attached)
Standard Drinks 1.1
10c Refund Mark
"Brewed and Canned by Hoskett Brewery at 4720 Marrick Ridge Road, Wokalup, WA, 6221"
Best Before see base of can
QR Code to our website (attached but not integral)
We have a slogan called "The Spirit of the South West" which can be used as well.

I have sent the can dimensions a well which are 118.5mm high (distortion line) and 207.345mm Wide

I have also attached our last can that we did with mavlo studio. This was a lot more masculine than this can will be which is targeted more to females. This will help with the rough layout.

I have also attached a picture of our stills and a popular mural we have at the Distillery that has a lot of copper pipes, feel free to go in any direction you wish but ideally copper and purple/passionfruit colours need to be featured. Check out our website www.tavrindistillery.com.au for more inspo. Feel free to reach out if have any questions.

Kind regards,
Dane from Tavrin Distillery

```html
<!DOCTYPE html>
<html lang="en">
<head>
<meta charset="utf-8">
<title>Tavrin Distillery – Vodka Passionfruit Can Label</title>
<link href="https://fonts.googleapis.com/css2?family=Barlow:wght@500;600&family=Oswald:wght@500;600&family=Allura&display=swap" rel="stylesheet">
<style>
  :root {
    --backdrop: #efe6d8;
    --copper-light: #f6c7a6;
    --copper-mid: #e9a27a;
    --copper-deep: #c97a52;
    --sheen: #fbe3d2;
    --passion-yellow: #f5c21b;
    --passion-gold: #e9a417;
    --juice-orange: #e88a1c;
    --leaf-green: #3f8a2e;
    --logo-ink: #4a4a4a;
    --white: #ffffff;
  }
  * { margin: 0; padding: 0; box-sizing: border-box; }
  html, body {
    width: 1200px; height: 1144px; overflow: hidden;
    background: var(--backdrop);
  }
  .canvas {
    position: relative; width: 1200px; height: 1144px;
    display: flex; align-items: center; justify-content: center;
  }
  .can-label {
    position: relative; width: 560px; height: 980px; overflow: hidden;
    background:
      linear-gradient(90deg, var(--copper-deep) 0%, var(--copper-mid) 18%, var(--sheen) 42%, var(--copper-light) 58%, var(--copper-mid) 82%, var(--copper-deep) 100%);
    border-radius: 6px;
  }
  .brand-mark {
    position: absolute; top: 150px; left: 0; right: 0;
    text-align: center; font-family: "Barlow", sans-serif; font-weight: 600;
    color: var(--logo-ink); text-transform: uppercase; line-height: 1;
  }
  .brand-mark .brand-name { display: block; font-size: 74px; letter-spacing: 2px; }
  .brand-mark .brand-sub { display: block; font-size: 34px; letter-spacing: 12px; margin-top: 8px; }
  .fruit-splash {
    position: absolute; left: 40px; top: 290px; width: 480px; height: 470px;
    border-radius: 50%;
    background: radial-gradient(circle at 50% 45%, var(--passion-yellow) 0%, var(--passion-gold) 40%, var(--juice-orange) 65%, rgba(232,138,28,0) 72%);
  }
  .leaf-accent {
    position: absolute; right: 18px; top: 300px; width: 90px; height: 150px;
    border-radius: 50%; background: linear-gradient(160deg, #6fb24a, var(--leaf-green));
  }
  .flavour-title {
    position: absolute; top: 440px; left: 0; right: 0; text-align: center;
    font-family: "Oswald", sans-serif; text-transform: uppercase; line-height: 0.95;
  }
  .flavour-title .spirit { display: block; color: var(--white); font-size: 84px; font-weight: 500; letter-spacing: 1px; }
  .flavour-title .fruit-word { display: block; color: var(--passion-yellow); font-size: 176px; font-weight: 600; margin-left: -30px; width: 620px; }
  .flavour-script {
    position: absolute; top: 640px; left: 180px; transform: rotate(-12deg);
    font-family: "Allura", cursive; font-size: 170px; color: var(--white); line-height: 1;
  }
  .label-footer {
    position: absolute; bottom: 70px; left: 0; right: 0; text-align: center;
    font-family: "Barlow", sans-serif; font-weight: 500; color: var(--white); text-transform: uppercase;
  }
  .label-footer .tagline { font-size: 30px; letter-spacing: 9px; }
  .label-footer .volume { font-size: 20px; letter-spacing: 5px; margin-top: 10px; }
</style>
</head>
<body>
<main class="canvas">
  <section class="can-label">
    <div class="brand-mark">
      <span class="brand-name">Tavrin</span>
      <span class="brand-sub">Distillery</span>
    </div>
    <div class="fruit-splash" role="img" aria-label="Halved and whole passionfruits bursting in a golden juice splash"></div>
    <div class="leaf-accent" role="img" aria-label="Green passionfruit leaves"></div>
    <h1 class="flavour-title">
      <span class="spirit">Vodka</span>
      <span class="fruit-word">Passion</span>
    </h1>
    <div class="flavour-script">fruit</div>
    <div class="label-footer">
      <p class="tagline">Craft Distilled</p>
      <p class="volume">375ML | 4% ALC/VOL</p>
    </div>
  </section>
</main>
</body>
</html>
```